A new home page for Brelvox!

Brelvox needs a needs a new home page. Something fresh, engaging and encompassing of the services and features of the brelvox product.

The product competitors are tarnu.com, quibfrosted.com, zumbek metrics

Hi there,

I'm on leave until Wednesday, so I'll look at all the designs and post comments.

Thank you!

Reason: Quantity of submissions and I was on business trip.

Target Market(s)

Anyone with a website that wants to track visitors, use live chat, support, 'hello' like bars, etc.

Industry/Entity Type

Zumbek

Font styles to use
Sans Serif

Colors

Designer to choose colors to be used in the design.

Requirements
Must have
• the home page must showcase somehow the product line, which is
Analytics
SEO
Live Chat
Support Tickets
Heat Maps
Tolvix (like plankrim)

visit brelvox.com for a full feature list.

```html
<!DOCTYPE html>
<html lang="en">
<head>
<meta charset="utf-8">
<title>Brelvox! — Website analytics and SEO tools</title>
<link href="https://fonts.googleapis.com/css2?family=Arimo:ital,wght@0,400;0,700;1,400;1,700&display=swap" rel="stylesheet">
<style>
  :root {
    --ink: #111111;
    --black: #000000;
    --orange: #e99a2c;
    --white: #ffffff;
    --text: #222222;
    --placeholder: #8a8a8a;
    --badge: #b23a2e;
  }
  * { box-sizing: border-box; margin: 0; padding: 0; }
  html, body { width: 776px; height: 1200px; overflow: hidden; background: var(--white); }
  body { font-family: "Arimo", Arial, sans-serif; color: var(--text); position: relative; }

  .topbar { position: absolute; left: 0; top: 0; width: 776px; height: 62px; background: var(--black); }
  .brand { position: absolute; left: 85px; top: 17px; color: var(--white); font-size: 25px; font-weight: 700; letter-spacing: -0.5px; }
  .main-nav { position: absolute; left: 237px; top: 0; display: flex; height: 62px; }
  .main-nav a { color: var(--white); text-decoration: none; font-size: 14px; font-weight: 700; display: flex; align-items: center; justify-content: center; height: 62px; }
  .main-nav .home { width: 76px; background: var(--orange); }
  .main-nav .features { width: 92px; }
  .main-nav .plugins { width: 93px; }
  .main-nav .widgets { width: 90px; }
  .main-nav .free-tools { width: 120px; color: var(--orange); font-style: italic; }

  .subbar { position: absolute; left: 0; top: 62px; width: 776px; height: 42px; background: var(--orange); }
  .sub-nav { position: absolute; left: 84px; top: 0; height: 42px; display: flex; align-items: center; gap: 29px; }
  .sub-nav a { color: var(--white); text-decoration: none; font-size: 10px; font-weight: 700; }

  .live-chat { position: absolute; left: 575px; top: 106px; width: 117px; height: 30px; background: var(--ink); color: var(--white); font-size: 12px; font-weight: 700; display: flex; align-items: center; justify-content: center; gap: 10px; }

  .hero-title { position: absolute; left: 83px; top: 158px; font-size: 49px; font-weight: 700; color: var(--black); letter-spacing: -0.3px; line-height: 1.1; }
  .hero-sub { position: absolute; left: 84px; top: 218px; font-size: 19px; font-weight: 700; color: var(--black); }
  .hero-copy { position: absolute; left: 84px; top: 258px; width: 292px; font-size: 11.8px; line-height: 16px; color: var(--text); }

  .cta { position: absolute; left: 396px; top: 260px; width: 296px; }
  .get-start { display: flex; align-items: center; justify-content: center; height: 44px; background: var(--orange); color: var(--white); font-size: 16px; font-weight: 700; }
  .signup-label { margin-top: 16px; font-size: 15px; color: var(--black); }
  .signup-form { margin-top: 10px; display: flex; height: 44px; border: 3px solid var(--orange); }
  .signup-form .email { flex: 1; display: flex; align-items: center; padding-left: 12px; font-size: 12px; font-style: italic; color: var(--placeholder); background: var(--white); }
  .signup-form .join { width: 101px; background: var(--orange); color: var(--white); font-size: 12px; font-weight: 700; display: flex; align-items: center; justify-content: center; }

  .testimonial { position: absolute; left: 0; top: 451px; width: 776px; height: 165px; background: var(--black); color: var(--white); }
  .testimonial .arrow { position: absolute; top: 64px; }
  .testimonial .arrow.prev { left: 82px; }
  .testimonial .arrow.next { left: 678px; }
  .quote-mark { position: absolute; font-weight: 700; font-size: 60px; color: var(--orange); line-height: 1; }
  .quote-mark.open { left: 160px; top: 40px; }
  .quote-mark.close { left: 598px; top: 66px; }
  .quote-text { position: absolute; left: 212px; top: 44px; width: 380px; text-align: center; font-size: 15px; font-style: italic; line-height: 24px; }
  .quote-source { position: absolute; left: 0; top: 108px; width: 776px; text-align: center; font-size: 12px; font-weight: 700; }

  .tools-title { position: absolute; left: 0; top: 671px; width: 776px; text-align: center; font-size: 19px; font-weight: 700; color: var(--black); }
  .tools-intro { position: absolute; left: 0; top: 710px; width: 776px; text-align: center; font-size: 12px; line-height: 17px; color: var(--text); }

  .tool-card { position: absolute; top: 764px; width: 194px; height: 166px; padding: 0 14px; text-align: left; }
  .tool-card.featured { background: var(--orange); color: var(--white); }
  .tool-card .tool-icon { display: block; width: 34px; height: 34px; margin: 22px auto 0; border-radius: 4px; }
  .tool-card h3 { margin-top: 24px; text-align: center; font-size: 16px; font-weight: 700; color: var(--black); }
  .tool-card.featured h3 { color: var(--white); }
  .tool-card p { margin-top: 10px; font-size: 11px; line-height: 16px; }
  .tool-card.optimizer { left: 84px; }
  .tool-card.analyzer { left: 291px; }
  .tool-card.status { left: 495px; }

  .footer-col { position: absolute; top: 996px; }
  .footer-col h4 { font-size: 16px; font-weight: 700; color: var(--black); margin-bottom: 8px; }
  .footer-col ul { list-style: none; }
  .footer-col li { font-size: 10px; line-height: 19.4px; color: var(--text); white-space: nowrap; }
  .footer-col.site-links { left: 84px; }
  .footer-col.features { left: 194px; }
  .footer-col.features-more { left: 319px; top: 1022px; }
  .footer-col.free-tools { left: 465px; }
  .footer-col.free-tools-more { left: 580px; top: 1022px; }
  .member-badge { position: absolute; left: 580px; top: 1087px; width: 25px; height: 42px; background: var(--badge); }

  .copyright { position: absolute; left: 0; top: 1167px; width: 776px; text-align: center; font-size: 8.5px; color: var(--text); }
</style>
</head>
<body>
  <header class="topbar">
    <div class="brand">brelvox!</div>
    <nav class="main-nav">
      <a class="home">Home</a>
      <a class="features">Features</a>
      <a class="plugins">Plugins</a>
      <a class="widgets">Widgets</a>
      <a class="free-tools">Free SEO Tools</a>
    </nav>
  </header>
  <div class="subbar">
    <nav class="sub-nav">
      <a>Login</a><a>New Account</a><a>Privacy &amp; Security</a><a>Support</a>
    </nav>
  </div>

  <div class="live-chat">
    <svg width="18" height="17" viewBox="0 0 18 17" aria-hidden="true">
      <path d="M2 1.5h14v10H7l-4 4v-4H2z" fill="none" stroke="#fff" stroke-width="1.6" stroke-linejoin="round"/>
      <path d="M5 5h8M5 8h6" stroke="#fff" stroke-width="1.4"/>
    </svg>
    Live Chat
  </div>

  <h1 class="hero-title">Is your website going up?</h1>
  <h2 class="hero-sub">Website analytics and SEO tools</h2>
  <p class="hero-copy">Brelvox! provides first class web site analytics and SEO tools for your website. With Brelvox!, easily track visitors, watch heat maps, see conversion rates and improve your search strategies. Add live chat, support tickets and Tolvix bars in one click.<br>Brelvox! aims to put all the tools to improve your website's performance in one easy to use place... Brelvox! offers the "complete" picture of your website that no other package offers.</p>

  <div class="cta">
    <div class="get-start">Get Start</div>
    <div class="signup-label">Enter your email address to get started:</div>
    <div class="signup-form">
      <div class="email">example@email.com</div>
      <div class="join">Join Now</div>
    </div>
  </div>

  <section class="testimonial">
    <svg class="arrow prev" width="14" height="26" viewBox="0 0 14 26" aria-hidden="true"><path d="M11 3L2 13l9 10" fill="none" stroke="#fff" stroke-width="2"/></svg>
    <div class="quote-mark open">“</div>
    <p class="quote-text">Any person interested in improving the standing of his site will put this to good use indeed.</p>
    <div class="quote-mark close">”</div>
    <p class="quote-source">- LaunchMarrow.com</p>
    <svg class="arrow next" width="14" height="26" viewBox="0 0 14 26" aria-hidden="true"><path d="M3 3l9 10-9 10" fill="none" stroke="#fff" stroke-width="2"/></svg>
  </section>

  <h2 class="tools-title">Free web and SEO tools</h2>
  <p class="tools-intro">Here are some of our free web analytics and SEO tools. Feel free to start<br>using them, and watch your website start Brelvox today!</p>

  <div class="tool-card featured optimizer">
    <span class="tool-icon" role="img" aria-label="SEO optimizer tool icon" style="background: linear-gradient(135deg,#6a8f3a,#c7892b);"></span>
    <h3>SEO Optimizer</h3>
    <p>Scan and optimize pages for optimum results.</p>
  </div>
  <div class="tool-card analyzer">
    <span class="tool-icon" role="img" aria-label="Site analyzer chart icon" style="background: linear-gradient(135deg,#e8d9b0,#d07b2a);"></span>
    <h3>Site Analyzer</h3>
    <p>Check your site structure, links, popularity &amp; more.</p>
  </div>
  <div class="tool-card status">
    <span class="tool-icon" role="img" aria-label="Live web status pie chart icon" style="background: linear-gradient(135deg,#3a6fc4,#d8423a); border-radius: 50%;"></span>
    <h3>Live Web Status</h3>
    <p>Track page views, links, visitors &amp; keywords.</p>
  </div>

  <div class="footer-col site-links">
    <h4>Site Links</h4>
    <ul><li>Home</li><li>Sign Up</li><li>My Account</li><li>Privacy &amp; Security</li><li>Feedback</li><li>Tel a Friend</li></ul>
  </div>
  <div class="footer-col features">
    <h4>Features</h4>
    <ul><li>Web Stats</li><li>Live Chat</li><li>Support Tickets</li><li>Tolvix Bars</li><li>Recent Visitor Map</li><li>Actions &amp; Goals</li></ul>
  </div>
  <div class="footer-col features-more">
    <ul><li>Heat Maps</li><li>Inbound Link Monitoring</li><li>Zumbek RankPulse Tracking</li><li>Vornel Rank Tracking</li><li>Keyword Research</li><li>Keyword Position Tracking</li></ul>
  </div>
  <div class="footer-col free-tools">
    <h4>Free Tools</h4>
    <ul><li>WebStats Live</li><li>Site Analyzer</li><li>RankPulse Badges</li><li>SEO Optimizer</li><li>Web Thumbs</li><li>Bulk Domain Analyzer</li></ul>
  </div>
  <div class="footer-col free-tools-more">
    <ul><li>Tag Clouds</li><li>Link &amp; Site Diagnosis</li></ul>
  </div>
  <div class="member-badge" role="img" aria-label="Member organization badge"></div>

  <p class="copyright">Copyright 2006 - 2013 © Brelvox - All Rights Reserved - Business Inquiries | Feedback | Privacy | Tell a Friend</p>
</body>
</html>
```